Web application layout remake

We are looking for a makeover on our web application called “QVLcrate” - it's a document management and digital archiving system integrating workflows and allowing you to free up physical space in your office currently occupied with documents by moving them to secure external custody.
We are expecting you to include the following:
• homepage
• signup page
• application page
This project is for the whole website (which is not big at all anyway!) and not just for the design of one page. The coding should be in HTML5 only.
We are aiming for fresh, appealing, clean, user friendly ,web 2.0, jquery layout.
Remakes or changes on the logo are welcome.
The application will be sold through the portal.
Please find in attachment the print screen of the application to aid you (this is the current view customers have after logging in but the layout is obsolete and we want a brand new!).
Reason: Still not happy with the received layouts. Keep up the good work! Thanks!
Reason: Still not happy with the whole solution and finding alternate app interfaces!
Industry/Entity Type
Digital
Look and feel
Each slider illustrates characteristics of the customer's brand and the style your logo design should communicate.

```html
<!DOCTYPE html>
<html lang="en">
<head>
<meta charset="utf-8">
<title>QVLcrate – Document Management System</title>
<link href="https://fonts.googleapis.com/css2?family=Source+Sans+3:ital,wght@0,400;0,600;0,700;1,400&display=swap" rel="stylesheet">
<style>
:root{
  --navy:#0b4a8a;
  --blue:#0e5aa7;
  --text-blue:#1d5fa8;
  --header-top:#0a4d93;
  --header-bottom:#0f63b3;
  --orange:#f58a0b;
  --orange-light:#ffa126;
  --green:#6aaa10;
  --green-light:#93cf12;
  --border:#d9dfe6;
}
*{box-sizing:border-box;margin:0;padding:0}
html,body{width:1085px;height:1200px;overflow:hidden;background:#fff;font-family:"Source Sans 3",sans-serif}
.page{position:relative;width:1085px;height:1200px;overflow:hidden}
.site-header{position:absolute;left:0;top:0;width:100%;height:91px;background:linear-gradient(180deg,var(--header-top),var(--header-bottom))}
.brand{position:absolute;left:75px;top:28px;display:flex;align-items:center;gap:10px;color:#fff;font-size:30px;font-weight:600}
.brand-mark{width:30px;height:30px;border-radius:50%;background:#fff}
.header-btn{position:absolute;top:34px;width:75px;height:32px;border-radius:3px;color:#fff;font-size:14px;display:flex;align-items:center;justify-content:center}
.btn-login{left:853px;background:#083a6b}
.btn-register{left:937px;background:#4f86c0}
.hero{position:absolute;left:0;top:91px;width:100%;height:404px;background:linear-gradient(180deg,#fff 0%,#e9f2fb 100%)}
.hero-title{position:absolute;left:73px;top:90px;color:var(--navy);font-weight:700;line-height:1.1}
.hero-title .l1{font-size:42px;display:block}
.hero-title .l2{font-size:35px;font-weight:600;display:block}
.hero-text{position:absolute;left:73px;top:180px;width:352px;color:var(--text-blue);font-size:12.5px;line-height:18.5px}
.btn-learn{position:absolute;left:73px;top:246px;width:97px;height:29px;background:linear-gradient(var(--orange-light),var(--orange));color:#fff;font-weight:700;font-size:13px;border-radius:2px;display:flex;align-items:center;justify-content:center}
.slider-arrows{position:absolute;left:73px;top:302px}
.hero-photo{position:absolute;left:429px;top:29px;width:231px;height:375px;background:linear-gradient(180deg,#d9c5b4 0%,#f1f1f1 45%,#e6e6e6 85%,#2a2a2a 100%);border-radius:110px 110px 0 0}
.trial{position:absolute;left:702px;top:37px;width:298px;height:339px;background:#fff;border:1px solid var(--border);border-radius:3px;overflow:hidden}
.trial-head{height:53px;background:linear-gradient(var(--header-bottom),var(--navy));color:#fff;font-size:22px;padding:14px 0 0 30px}
.trial-sub{font-size:12px;color:#555;margin:20px 0 0 30px}
.field{position:absolute;left:26px;width:246px;height:33px;border:1px solid #cfd6de;border-radius:2px;font-size:14px;color:#999;padding:7px 15px}
.btn-start{position:absolute;left:160px;top:273px;width:110px;height:33px;border-radius:3px;background:linear-gradient(var(--orange-light),var(--orange));color:#fff;font-size:16px;font-weight:600;display:flex;align-items:center;justify-content:center}
.package{position:absolute;top:523px;width:231px;height:173px;border-radius:2px;color:#fff;padding:16px 26px}
.package h3{font-size:27px;font-weight:400}
.package h3 span{font-size:18px}
.package .spec{font-size:14px;margin-top:2px}
.package .note{font-size:11.5px;opacity:.65;margin-top:8px;line-height:17px}
.package .price{font-size:25px;margin-top:6px}
.package .price small{font-size:14px}
.pkg-bronze{left:63px;background:linear-gradient(#3b84c7,#063f82)}
.pkg-silver{left:308px;background:linear-gradient(#3b84c7,#063f82)}
.pkg-gold{left:551px;background:linear-gradient(var(--orange-light),var(--orange))}
.pkg-platinum{left:794px;background:linear-gradient(var(--green-light),var(--green))}
.welcome{position:absolute;left:60px;top:758px;width:655px;color:var(--text-blue)}
.welcome h2{font-size:26px;font-weight:600;color:var(--blue);margin-bottom:12px}
.welcome p{font-size:12.8px;line-height:18.9px;margin-bottom:16px}
.testimonials{position:absolute;left:755px;top:742px;width:270px;height:269px;border:1px solid var(--border);border-radius:3px}
.testimonials h3{height:48px;background:linear-gradient(#fff,#f0f0f0);font-size:21px;font-weight:400;color:#333;padding:12px 22px}
.quote{margin:20px 22px 0 22px;font-style:italic;font-size:12.5px;color:#555;line-height:17px}
.quote cite{display:block;font-style:normal;font-weight:600;color:var(--orange);margin-top:6px}
.site-footer{position:absolute;left:0;top:1065px;width:100%;height:135px;background:linear-gradient(#f5f7fa,#fff)}
.copyright{position:absolute;left:67px;top:38px;font-size:13.5px;color:#7a98b8}
.social{position:absolute;left:934px;top:30px;display:flex;gap:4px}
.social span{width:24px;height:24px;border-radius:3px}
</style>
</head>
<body>
<div class="page">
  <header class="site-header">
    <div class="brand"><span class="brand-mark"></span>QVLcrate</div>
    <div class="header-btn btn-login">Login</div>
    <div class="header-btn btn-register">Register</div>
  </header>

  <section class="hero">
    <h1 class="hero-title"><span class="l1">DOCUMENT</span><span class="l2">MANAGEMENT SYSTEM</span></h1>
    <p class="hero-text">Mauris vel lacus vitae felis vestibulum volutpat. Etiam est nunc, venenatis in, tristique eu, imperdiet ac, nisl. Cum sociis natoque penatibus et magnis dis parturient montes</p>
    <div class="btn-learn">LEARN MORE</div>
    <svg class="slider-arrows" width="36" height="24" viewBox="0 0 36 24"><path d="M12 2 3 12l9 10M22 2l9 10-9 10" fill="none" stroke="#0e5aa7" stroke-width="2.2"/></svg>
    <div class="hero-photo" role="img" aria-label="Photo of a smiling businesswoman in a white shirt with arms crossed"></div>
    <form class="trial">
      <div class="trial-head">Start Free Trail Now</div>
      <p class="trial-sub">You'll be up and running in less than a minute.</p>
      <div class="field" style="top:99px">Your name</div>
      <div class="field" style="top:143px">Company or organization</div>
      <div class="field" style="top:187px">Email address</div>
      <div class="field" style="top:230px">Password</div>
      <div class="btn-start">Start Now</div>
    </form>
  </section>

  <div class="package pkg-bronze"><h3>Bronze <span>Package</span></h3><p class="spec">10 GB Space &amp; 5 Users</p><p class="note">Nunc tempus felis vitae urna. Viva-<br>mus porttitor, g, purus nisi</p><p class="price">$15.<small>99</small></p></div>
  <div class="package pkg-silver"><h3>Silver <span>Package</span></h3><p class="spec">25 GB Space &amp; 10 Users</p><p class="note">Nunc tempus felis vitae urna. Viva-<br>mus porttitor, g, purus nisi</p><p class="price">$20.<small>99</small></p></div>
  <div class="package pkg-gold"><h3>Gold <span>Package</span></h3><p class="spec">50 GB Space &amp; 15 Users</p><p class="note">Nunc tempus felis vitae urna. Viva-<br>mus porttitor, g, purus nisi</p><p class="price">$25.<small>00</small></p></div>
  <div class="package pkg-platinum"><h3>Platinum <span>Package</span></h3><p class="spec">100 GB Space &amp; 25 Users</p><p class="note">Nunc tempus felis vitae urna. Viva-<br>mus porttitor, g, purus nisi</p><p class="price">$30.<small>99</small></p></div>

  <section class="welcome">
    <h2>Welcome to Our Website Mainpage..</h2>
    <p>Duis tincidunt lectus quis dui viverra vestibulum. Suspendisse vulputate aliquam dui. Nulla elementum dui ut augue. Aliquam vehicula mi at mauris. Maecenas placerat, nisl at consequat rhoncus, sem nunc gravida justo, quis eleifend arcu velit quis lacus. Morbi magna magna, tincidunt a, mattis non, imperdiet vitae, tellus. Sed odio est, auctor ac, sollicitudin in, consequat vitae, orci. Fusce id felis. Vivamus sollicitudin metus eget eros.</p>
    <p>Mauris vel lacus vitae felis vestibulum volutpat. Etiam est nunc, venenatis in, tristique eu, imperdiet ac, nisl. Cum sociis natoque penatibus et magnis dis parturient montes, nascetur ridiculus mus. In iaculis facilisis massa.</p>
    <p>Etiam eu urna. Sed porta. Suspendisse quam leo, molestie sed, luctus quis, feugiat in, pede. Fusce tellus. Sed metus augue, convallis et, vehicula ut, pulvinar eu, ante. Integer orci tellus, tristique vitae, consequat nec</p>
  </section>

  <aside class="testimonials">
    <h3>Customer Testimonials</h3>
    <blockquote class="quote">Duis sed tellus et tortor vestibulum gravida. Praesent elementum elit at tellus.<cite>by Author Name</cite></blockquote>
    <blockquote class="quote" style="margin-top:26px">Maecenas aliquet velit vel turpis. Mauris neque metus, malesuada nec, ultricies sit amet, porttitor mattis<cite>by Author Name</cite></blockquote>
  </aside>

  <footer class="site-footer">
    <p class="copyright">© 2013 Company Name.&nbsp; All right reserved.&nbsp; Term of Use</p>
    <div class="social"><span style="background:#2aa3e0"></span><span style="background:#1a6aa8"></span><span style="background:#3b5ea8"></span></div>
  </footer>
</div>
</body>
</html>
```